Rebrand stationary with recently completed logo design

Need new business cards, thank you cards, letterhead, envelopes and presentation folders. The designs will be sent to a separate production firm so I need the files to be print ready.

My contact info
Reno Vasquell

Office 604-381-5047
Fax 604-317-4860

Email reno@glazemark.ca
website www.glazemark.ca

315-20740 47th Avenue,
Langley, BC, V2K 3P8

Target Market(s)

Homeowners, businesses and contractors

Industry/Entity Type

Business

Font styles to use
Sans Serif

Colors
34a7d7

Requirements
Must have
• Like to have one side of the business card a solid color with the logo in all white. The side with all the text to be a white background
• I find the current blue on the front of the card with the white logo too dark.
Should not have
• Gradient colors

```html
<!DOCTYPE html>
<html lang="en">
<head>
<meta charset="utf-8">
<title>Glazemark Business Card</title>
<link rel="stylesheet" href="https://fonts.googleapis.com/css2?family=Open+Sans:wght@400;600&display=swap">
<style>
  :root {
    --backdrop: #e7e4df;
    --card-white: #f7f7f7;
    --slate: #465862;
    --brand-blue: #34a7d7;
    --text-grey: #4a5258;
    --tagline-grey: #8e979d;
    --tagline-light: #9aa5ac;
    --white: #ffffff;
  }
  * { margin: 0; padding: 0; box-sizing: border-box; }
  html, body {
    width: 1200px;
    height: 960px;
    overflow: hidden;
    background: var(--backdrop);
    font-family: "Open Sans", sans-serif;
  }
  .canvas { position: relative; width: 1200px; height: 960px; }

  .card {
    position: absolute;
    width: 600px;
    height: 341px;
    box-shadow: 0 2px 6px rgba(0,0,0,0.25);
  }
  .card--front { left: 302px; top: 130px; background: var(--card-white); }
  .card--back  { left: 299px; top: 488px; background: var(--slate); }

  .front-band {
    position: absolute;
    left: 0; top: 0;
    width: 176px; height: 100%;
    background: var(--slate);
  }

  .front-details {
    position: absolute;
    right: 40px;
    top: 52px;
    text-align: right;
    color: var(--text-grey);
  }
  .wordmark {
    font-weight: 600;
    color: var(--brand-blue);
    letter-spacing: 0.5px;
    line-height: 1;
    white-space: nowrap;
  }
  .front-details .wordmark { font-size: 38px; }
  .tagline {
    font-size: 13.5px;
    letter-spacing: 1.6px;
    color: var(--tagline-grey);
    line-height: 1;
    margin-top: 6px;
    white-space: nowrap;
  }
  .person-name {
    font-size: 17px;
    font-weight: 600;
    color: var(--brand-blue);
    margin-top: 24px;
    line-height: 1.1;
  }
  .contact-line { font-size: 13px; line-height: 18px; white-space: nowrap; }
  .contact-block { margin-top: 12px; }

  .back-lockup {
    position: absolute;
    left: 125px;
    top: 110px;
    display: flex;
    align-items: center;
    gap: 20px;
  }
  .back-square {
    width: 44px; height: 44px;
    background: var(--white);
  }
  .back-lockup .wordmark { font-size: 44px; color: var(--white); }
  .back-lockup .tagline { font-size: 15px; color: var(--tagline-light); letter-spacing: 1.8px; }
</style>
</head>
<body>
<div class="canvas">
  <section class="card card--front">
    <div class="front-band"></div>
    <div class="front-details">
      <div class="wordmark">GLAZEMARK</div>
      <div class="tagline">GLASS FILM SPECIALISTS</div>
      <div class="person-name">RENO VASQUELL</div>
      <div class="contact-line">reno@glazemark.ca</div>
      <div class="contact-block">
        <div class="contact-line">315-20740 47th Avenue</div>
        <div class="contact-line">Langley, BC, V2K 3P8</div>
      </div>
      <div class="contact-block">
        <div class="contact-line">(Office) 604-381-5047</div>
        <div class="contact-line">(Fax) 604-317-4860</div>
        <div class="contact-line">(Web) www.glazemark.ca</div>
      </div>
    </div>
  </section>

  <section class="card card--back">
    <div class="back-lockup">
      <div class="back-square"></div>
      <div>
        <div class="wordmark">GLAZEMARK</div>
        <div class="tagline">GLASS FILM SPECIALISTS</div>
      </div>
    </div>
  </section>
</div>
</body>
</html>
```